Business card design needed

www.corvanfab.com.au
Our primary services:
On-site welding.
On-site industrial maintenance.
On-site repairs and capital works projects specialising in pipe fabrication.
Our ability to work on-site with our dedicated mobile equipment is essential to our capability to provide a quality maintenance service to our customers. We are capable of providing a full team of qualified boilermakers that can work either to your plan or project manage if a plan has not been developed.
Industry/Entity Type
Industrial
Contact Information for Business Card
company name- CORVAN FAB PTY LTD
story - industrial steel fabrication, constructions and pipelines
Director - Greg Halvey
workshop address - shed 7, 3820 mirren rd Tully
postal address - P.O BOX 268 TULLY Q 4854
mobile - 0438596204
w/shop phone - 0740593827
fax - 0740593828
email - admin@corvanfab.com.au
web - www.corvanfab.com.au
Logo Text
CORVAN FAB pty ltd

```html
<!DOCTYPE html>
<html lang="en">
<head>
<meta charset="utf-8">
<title>Corvan Fab – Business Card</title>
<link rel="stylesheet" href="https://fonts.googleapis.com/css2?family=Montserrat:wght@400;500;600&display=swap">
<style>
  :root {
    --backdrop: #e9e6e2;
    --plate-dark: #0c0c0c;
    --plate-mid: #2a2a2a;
    --panel-grey: #3b3b3b;
    --panel-grey-light: #474747;
    --ink-white: #ffffff;
    --ink-soft: #d9d9d9;
    --shadow: rgba(0, 0, 0, 0.28);
  }
  * { box-sizing: border-box; margin: 0; padding: 0; }
  html, body {
    width: 1200px;
    height: 839px;
    overflow: hidden;
    background: var(--backdrop);
    font-family: "Montserrat", Arial, sans-serif;
  }
  .canvas {
    width: 1200px;
    height: 839px;
    display: flex;
    align-items: center;
    justify-content: center;
    gap: 40px;
  }
  .card {
    position: relative;
    width: 540px;
    height: 309px;
    overflow: hidden;
    box-shadow: 0 10px 24px var(--shadow);
    color: var(--ink-white);
  }
  .plate-texture {
    position: absolute;
    inset: 0;
    background: radial-gradient(ellipse at 35% 30%, var(--plate-mid), var(--plate-dark) 75%);
  }

  /* Back face */
  .card-back .brand {
    position: absolute;
    right: 46px;
    top: 92px;
    text-align: right;
  }
  .card-back .brand-name {
    display: flex;
    align-items: center;
    gap: 12px;
    font-size: 40px;
    font-weight: 500;
    letter-spacing: 2px;
    line-height: 1;
  }
  .brand-mark {
    width: 16px;
    height: 16px;
    background: var(--ink-white);
  }
  .card-back .website {
    margin-top: 18px;
    font-size: 15px;
    font-weight: 400;
    letter-spacing: 1px;
    color: var(--ink-soft);
  }

  /* Front face */
  .card-front .identity {
    position: absolute;
    left: 24px;
    top: 58px;
    width: 300px;
    text-align: right;
  }
  .identity .person-name {
    font-size: 30px;
    font-weight: 500;
    letter-spacing: 1.5px;
    line-height: 1.1;
  }
  .identity .person-role {
    font-size: 14px;
    font-weight: 400;
    letter-spacing: 1.5px;
    margin-top: 2px;
  }
  .contact-panel {
    position: absolute;
    top: 0;
    right: 0;
    width: 200px;
    height: 100%;
    background: linear-gradient(160deg, var(--panel-grey-light), var(--panel-grey));
    padding: 66px 0 0 22px;
  }
  .contact-list { list-style: none; }
  .contact-list li {
    display: flex;
    align-items: center;
    gap: 10px;
    height: 22px;
    margin-bottom: 16px;
    font-size: 12px;
    font-weight: 400;
    letter-spacing: 0.5px;
  }
  .contact-icon {
    width: 20px;
    height: 20px;
    flex: none;
  }
  .contact-panel .brand {
    position: absolute;
    right: 22px;
    bottom: 22px;
    display: flex;
    align-items: center;
    gap: 7px;
    font-size: 16px;
    font-weight: 500;
    letter-spacing: 1px;
  }
  .contact-panel .brand-mark { width: 9px; height: 9px; }
</style>
</head>
<body>
<main class="canvas">

  <section class="card card-back" aria-label="Business card back">
    <div class="plate-texture" role="img" aria-label="Dark diamond-plate steel texture"></div>
    <div class="brand">
      <div class="brand-name"><span class="brand-mark"></span>CORVAN FAB</div>
      <div class="website">www.corvanfab.com.au</div>
    </div>
  </section>

  <section class="card card-front" aria-label="Business card front">
    <div class="plate-texture" role="img" aria-label="Dark diamond-plate steel texture"></div>
    <div class="identity">
      <div class="person-name">YOUR NAME</div>
      <div class="person-role">YOUR PROFILE</div>
    </div>
    <aside class="contact-panel">
      <ul class="contact-list">
        <li>
          <svg class="contact-icon" viewBox="0 0 20 20" aria-hidden="true">
            <rect width="20" height="20" rx="2" fill="#fff"/>
            <path d="M6 4.5l2 2.2-1.1 1.6c.8 1.7 2 2.9 3.7 3.8l1.6-1.1 2.2 2-1.3 1.9C9 14.5 5.6 11.1 5 6z" fill="#3b3b3b"/>
          </svg>
          <span>+123.456.789</span>
        </li>
        <li>
          <svg class="contact-icon" viewBox="0 0 20 20" aria-hidden="true">
            <rect width="20" height="20" rx="2" fill="#fff"/>
            <path d="M7 5h6a1 1 0 0 1 1 1v9a1 1 0 0 1-1 1H7a1 1 0 0 1-1-1V6a1 1 0 0 1 1-1z" fill="#3b3b3b"/>
            <rect x="7.5" y="6.5" width="5" height="6.5" fill="#fff"/>
          </svg>
          <span>+123.456.789</span>
        </li>
        <li>
          <svg class="contact-icon" viewBox="0 0 20 20" aria-hidden="true">
            <rect width="20" height="20" rx="2" fill="#fff"/>
            <rect x="3.5" y="6" width="13" height="9" fill="none" stroke="#3b3b3b" stroke-width="1.3"/>
            <path d="M3.5 6l6.5 5 6.5-5" fill="none" stroke="#3b3b3b" stroke-width="1.3"/>
          </svg>
          <span>your@email.com</span>
        </li>
      </ul>
      <div class="brand"><span class="brand-mark"></span>CORVAN FAB</div>
    </aside>
  </section>

</main>
</body>
</html>
```